Design new Postwren Template for our company newsletters

We are currently using postwren (www.postwren-mail.com)to send out emails/newsletters to our client database.
The postwren template we have been using is looking a little tired and in light of the fact that we have just redesigned our website and other marketing material we would like a new postwren template which is more in line with our new look.
Our new logo should be used in the template rather than the current 'kaleidoscope multi coloured green shaded logo' which is presently being used. Our new logo is included as an attachment to this brief.
The colours we use in our marketing material have recently been changed. Please refer to our website www.quillbrookadvisory.com.au for an indication of our preferred colours/style.
I have tried to download and save our current template and have attached to brief (please disregard content inside newsletter).
I have also attached a copy of a recent email newsletter sent via postwren to our clients. Again, please disregard the content of the newsletter.
Please message me if any further info is required. Thanks, Bette
Reason: Other urgent matters have meant management have not had sufficient opportunity to look at designs submitted
Marketing

```html
<!DOCTYPE html>
<html lang="en">
<head>
<meta charset="utf-8">
<title>Quillbrook Advisory Partner Update</title>
<link rel="stylesheet" href="https://fonts.googleapis.com/css2?family=Oswald:wght@500;700&family=Open+Sans:wght@400;700&display=swap">
<style>
  :root {
    --brand-green: #97bf0d;
    --heading-green: #8cb400;
    --list-green: #6b8f00;
    --ink: #555555;
    --ink-dark: #333333;
    --title-grey: #9a9a9a;
    --frame: #cfcfcf;
    --page-light: #f2f2f2;
    --page-dark: #bdbdbd;
    --white: #ffffff;
  }
  * { box-sizing: border-box; margin: 0; padding: 0; }
  html, body { width: 1200px; height: 900px; overflow: hidden; }
  body {
    background: radial-gradient(ellipse at 50% 90%, var(--page-light) 0%, #dcdcdc 50%, var(--page-dark) 100%);
    font-family: "Open Sans", Verdana, sans-serif;
    position: relative;
  }
  .newsletter {
    position: absolute; left: 397px; top: 11px; width: 440px; height: 862px;
    background: var(--white);
  }
  .masthead {
    height: 45px; background: var(--brand-green); position: relative;
  }
  .brand-name {
    position: absolute; left: 19px; top: 9px;
    font-family: "Oswald", sans-serif; font-weight: 700; font-size: 21px; letter-spacing: 0.5px;
    color: var(--ink-dark); line-height: 26px;
  }
  .masthead-phone { position: absolute; right: 14px; top: 6px; text-align: right; color: var(--ink-dark); }
  .masthead-phone .label { font-size: 7.5px; letter-spacing: 0.6px; }
  .masthead-phone .number { font-family: "Oswald", sans-serif; font-weight: 500; font-size: 13px; letter-spacing: 0.6px; margin-top: 3px; }
  .update-title {
    position: absolute; top: 51px; left: 0; width: 100%; text-align: center;
    font-family: "Oswald", sans-serif; font-weight: 700; font-size: 19px; color: var(--title-grey); line-height: 24px;
  }
  .panel {
    position: absolute; left: 18px; width: 403px;
    border: 1px solid var(--frame); border-radius: 7px; background: var(--white);
    font-size: 10.6px; line-height: 15.4px; color: var(--ink); text-align: justify;
  }
  .lenders { top: 78px; height: 87px; display: flex; align-items: center; justify-content: center; gap: 22px; }
  .lender {
    display: flex; align-items: center; gap: 5px;
    font-family: "Open Sans", sans-serif; font-weight: 700; font-size: 11px; color: var(--ink-dark); line-height: 13px; text-align: left;
  }
  .lender .mark { width: 12px; height: 12px; background: var(--heading-green); flex: none; }
  .lender .mark.round { border-radius: 50%; }
  .section-head {
    position: absolute; display: flex; align-items: center; gap: 8px;
    font-family: "Oswald", sans-serif; font-weight: 700; font-size: 21px; color: var(--heading-green); line-height: 24px;
  }
  .section-head svg { width: 34px; height: 34px; flex: none; }
  .panel p + p { margin-top: 15px; }
  .intro { top: 215px; height: 200px; padding: 7px 10px; }
  .solutions { top: 467px; height: 231px; padding: 6px 11px; }
  .contact { top: 750px; height: 57px; padding: 5px 6px; }
  .benefits { list-style: none; margin-top: 12px; margin-left: 5px; }
  .benefits li {
    display: flex; align-items: center; gap: 8px;
    font-weight: 700; color: var(--list-green); line-height: 19px; font-size: 10.6px;
  }
  .benefits svg { width: 11px; height: 11px; flex: none; }
  .footer {
    position: absolute; left: 0; bottom: 0; width: 100%; height: 45px; background: var(--brand-green);
  }
  .copyright { position: absolute; left: 22px; bottom: 7px; font-size: 9px; color: var(--ink-dark); }
  .follow { position: absolute; right: 14px; top: 6px; text-align: center; }
  .follow .label { font-family: "Oswald", sans-serif; font-weight: 700; font-size: 9px; color: var(--white); letter-spacing: 0.3px; }
  .social { display: flex; gap: 4px; margin-top: 3px; }
  .social span { width: 14px; height: 14px; border-radius: 50%; border: 1.5px solid var(--white); }
</style>
</head>
<body>
<main class="newsletter">
  <header class="masthead">
    <div class="brand-name">QUILLBROOK ADVISORY</div>
    <div class="masthead-phone">
      <div class="label">PHONE US TODAY!</div>
      <div class="number">1300 555 014</div>
    </div>
  </header>

  <h1 class="update-title">QUILLBROOK PARTNER UPDATE</h1>

  <section class="panel lenders" aria-label="Lending partners">
    <div class="lender"><span class="mark"></span>Harbourline<br>Finance</div>
    <div class="lender"><span class="mark"></span>Saltbush</div>
    <div class="lender"><span class="mark round"></span>Southern Keystone<br>Mortgage</div>
  </section>

  <h2 class="section-head" style="left:13px; top:173px;">
    <svg viewBox="0 0 34 34"><circle cx="17" cy="17" r="16" fill="var(--heading-green)"/><circle cx="17" cy="17" r="11" fill="#fff"/><circle cx="17" cy="17" r="9.5" fill="var(--heading-green)"/><path d="M12 17.5l3.5 3.5 7-8" stroke="#fff" stroke-width="3" fill="none" stroke-linecap="round" stroke-linejoin="round"/></svg>
    CREDIT IMPAIRED LENDING
  </h2>
  <section class="panel intro">
    <p>Quillbrook Advisory can provide access to a range of solutions for clients who fall outside normal lending criteria for Banks and Mortgage Insurers.</p>
    <p>Harbourline Finance, Saltbush Home Loans and Southern Keystone Mortgage are three of Australia’s leading credit impaired lending providers with a broad range of products and solutions. These lenders specialise in providing solutions to clients who have been unable to satisfy the lending criteria of traditional lenders.</p>
    <p>Quillbrook Advisory is pleased to partner with Harbourline, Saltbush and Southern Keystone Mortgage and be able to provide these services via an exclusive arrangement for our mortgage referral partners.</p>
  </section>

  <h2 class="section-head" style="left:21px; top:420px;">
    <svg viewBox="0 0 34 34"><circle cx="17" cy="17" r="16" fill="var(--heading-green)"/><circle cx="17" cy="17" r="11" fill="#fff"/><circle cx="17" cy="17" r="9.5" fill="var(--heading-green)"/><path d="M12 17.5l3.5 3.5 7-8" stroke="#fff" stroke-width="3" fill="none" stroke-linecap="round" stroke-linejoin="round"/></svg>
    CREDIT IMPAIRED SOLUTIONS
  </h2>
  <section class="panel solutions">
    <p>Harbourline Finance, Saltbush Home Loans and Southern Keystone Mortgage have a broad range of lending products available for your clients.</p>
    <ul class="benefits">
      <li><svg viewBox="0 0 11 11"><circle cx="5.5" cy="5.5" r="5.5" fill="var(--heading-green)"/><path d="M3 5.8l1.7 1.6 3.3-3.6" stroke="#fff" stroke-width="1.5" fill="none"/></svg>Multiple debt consolidation</li>
      <li><svg viewBox="0 0 11 11"><circle cx="5.5" cy="5.5" r="5.5" fill="var(--heading-green)"/><path d="M3 5.8l1.7 1.6 3.3-3.6" stroke="#fff" stroke-width="1.5" fill="none"/></svg>Current mortgage arrears considered</li>
      <li><svg viewBox="0 0 11 11"><circle cx="5.5" cy="5.5" r="5.5" fill="var(--heading-green)"/><path d="M3 5.8l1.7 1.6 3.3-3.6" stroke="#fff" stroke-width="1.5" fill="none"/></svg>Past credit issues considered</li>
      <li><svg viewBox="0 0 11 11"><circle cx="5.5" cy="5.5" r="5.5" fill="var(--heading-green)"/><path d="M3 5.8l1.7 1.6 3.3-3.6" stroke="#fff" stroke-width="1.5" fill="none"/></svg>Low doc loans for self employed</li>
      <li><svg viewBox="0 0 11 11"><circle cx="5.5" cy="5.5" r="5.5" fill="var(--heading-green)"/><path d="M3 5.8l1.7 1.6 3.3-3.6" stroke="#fff" stroke-width="1.5" fill="none"/></svg>No Lenders mortgage insurance</li>
      <li><svg viewBox="0 0 11 11"><circle cx="5.5" cy="5.5" r="5.5" fill="var(--heading-green)"/><path d="M3 5.8l1.7 1.6 3.3-3.6" stroke="#fff" stroke-width="1.5" fill="none"/></svg>Refinances of existing low doc and credit impaired loans</li>
      <li><svg viewBox="0 0 11 11"><circle cx="5.5" cy="5.5" r="5.5" fill="var(--heading-green)"/><path d="M3 5.8l1.7 1.6 3.3-3.6" stroke="#fff" stroke-width="1.5" fill="none"/></svg>Broad range of acceptable security</li>
      <li><svg viewBox="0 0 11 11"><circle cx="5.5" cy="5.5" r="5.5" fill="var(--heading-green)"/><path d="M3 5.8l1.7 1.6 3.3-3.6" stroke="#fff" stroke-width="1.5" fill="none"/></svg>Commercial loans</li>
      <li><svg viewBox="0 0 11 11"><circle cx="5.5" cy="5.5" r="5.5" fill="var(--heading-green)"/><path d="M3 5.8l1.7 1.6 3.3-3.6" stroke="#fff" stroke-width="1.5" fill="none"/></svg>Refinance tax office debts</li>
    </ul>
  </section>

  <h2 class="section-head" style="left:21px; top:710px;">
    <svg viewBox="0 0 34 34"><circle cx="17" cy="17" r="16" fill="var(--heading-green)"/><circle cx="17" cy="17" r="11" fill="#fff"/><circle cx="17" cy="17" r="9.5" fill="var(--heading-green)"/><path d="M12 17.5l3.5 3.5 7-8" stroke="#fff" stroke-width="3" fill="none" stroke-linecap="round" stroke-linejoin="round"/></svg>
    NEED MORE INFORMATION?
  </h2>
  <section class="panel contact">
    <p>To discuss a loan scenario, or for an introduction to a credit impaired specialist, please call our office on 1300 555 014 or speak to your local Quillbrook Advisory Relationship Manager.</p>
  </section>

  <footer class="footer">
    <div class="copyright">Copyright © *2013 QUILLBROOK Advisory, All rights reserved.</div>
    <div class="follow">
      <div class="label">FOLLOW US</div>
      <div class="social" aria-label="Social links"><span></span><span></span><span></span></div>
    </div>
  </footer>
</main>
</body>
</html>
```